Bref créative
Business Card for ecommerce technology company
Circuitry Supply Partners, LLC.
Professional
Paul Dunmore
President
457 Ridgeback Ave.
Fernvale, QX 58204
mark@quorvix.com
www.quorvix.com
Please send Business card so I will be able to edit it for other employees

```html
<!DOCTYPE html>
<html lang="en">
<head>
<meta charset="utf-8">
<title>Quorvix Stationery</title>
<link href="https://fonts.googleapis.com/css2?family=Arimo:wght@400;700&display=swap" rel="stylesheet">
<style>
  :root {
    --bg: #e9eaec;
    --paper: #ffffff;
    --blue: #1769d1;
    --blue-light: #3c9bf0;
    --blue-dark: #0b3f96;
    --ink: #222a35;
    --muted: #5d6672;
    --line: #0d0d0d;
  }
  * { margin: 0; padding: 0; box-sizing: border-box; }
  html, body { width: 1200px; height: 936px; overflow: hidden; }
  body { background: var(--bg); font-family: "Arimo", Arial, sans-serif; color: var(--ink); position: relative; }
  .sheet { position: absolute; background: var(--paper); box-shadow: 0 2px 8px rgba(0,0,0,.12); overflow: hidden; }
  .wave { position: absolute; left: 0; bottom: 0; width: 100%; display: block; }
  .brand { font-weight: 700; color: var(--blue); letter-spacing: .02em; line-height: 1; }
  .tagline { color: var(--muted); font-size: 9px; line-height: 1.2; }
  .dot { border-radius: 50%; background: radial-gradient(circle at 35% 35%, var(--blue-light), var(--blue-dark)); position: absolute; }

  /* Letterhead */
  .letterhead { left: 178px; top: 64px; width: 432px; height: 609px; }
  .letterhead .logo { position: absolute; left: 30px; top: 30px; display: flex; align-items: center; gap: 8px; }
  .letterhead .logo .dot { position: static; width: 34px; height: 34px; }
  .letterhead .brand { font-size: 24px; }
  .letterhead .contact { position: absolute; left: 290px; top: 30px; font-size: 8px; line-height: 1.55; color: var(--muted); list-style: none; }
  .letterhead .contact li::before { content: ""; display: inline-block; width: 5px; height: 5px; border-radius: 50%; background: var(--blue); margin-right: 5px; vertical-align: middle; }
  .letterhead .faint-mark { left: 160px; top: 190px; width: 112px; height: 112px; opacity: .18; }

  /* Folder */
  .folder { left: 635px; top: 51px; width: 521px; height: 640px; }
  .folder .dot { left: 197px; top: 200px; width: 127px; height: 127px; }
  .folder .name { position: absolute; top: 352px; width: 100%; text-align: center; }
  .folder .brand { font-size: 50px; }
  .folder .tagline { font-size: 17px; margin-top: 6px; color: var(--ink); }

  /* Business cards */
  .card { left: 36px; width: 218px; height: 78px; }
  .card-front { top: 730px; }
  .card-front .logo { position: absolute; left: 10px; top: 10px; display: flex; align-items: center; gap: 5px; }
  .card-front .logo .dot { position: static; width: 16px; height: 16px; }
  .card-front .brand { font-size: 13px; }
  .card-front .details { position: absolute; left: 12px; top: 34px; font-size: 5px; line-height: 1.4; color: var(--muted); }
  .card-front .details strong { color: var(--ink); font-size: 6px; }
  .card-back { top: 814px; }
  .card-back .dot { left: 20px; top: 14px; width: 32px; height: 32px; }
  .card-back .web { position: absolute; left: 18px; top: 52px; font-size: 6px; color: var(--muted); }

  /* Envelopes */
  .envelope { top: 742px; height: 172px; }
  .envelope-front { left: 267px; width: 457px; }
  .envelope-front .logo { position: absolute; left: 16px; top: 20px; display: flex; align-items: center; gap: 6px; }
  .envelope-front .logo .dot { position: static; width: 26px; height: 26px; }
  .envelope-front .brand { font-size: 18px; }
  .envelope-front .return { position: absolute; left: 18px; top: 56px; font-size: 7px; color: var(--muted); }
  .envelope-back { left: 737px; width: 436px; }
  .envelope-back .flap { position: absolute; inset: 0; width: 100%; height: 100%; }
  .envelope-back .web { position: absolute; top: 34px; width: 100%; text-align: center; font-size: 9px; letter-spacing: .3em; color: #fff; }
</style>
</head>
<body>

<section class="sheet letterhead" aria-label="Letterhead">
  <div class="logo"><span class="dot"></span>
    <div><div class="brand">QUORVIX</div><div class="tagline">Circuitry Supply Partners, LLC.</div></div>
  </div>
  <ul class="contact">
    <li>457 Ridgeback Ave.</li>
    <li>Fernvale, QX 58204</li>
    <li>555-010-2040</li>
    <li>555-010-2041</li>
    <li>mark@quorvix.com</li>
    <li>www.quorvix.com</li>
  </ul>
  <span class="dot faint-mark"></span>
  <svg class="wave" viewBox="0 0 400 110" preserveAspectRatio="none" height="110">
    <defs><linearGradient id="gLh" x1="0" y1="0" x2="0" y2="1"><stop offset="0" stop-color="#3c9bf0"/><stop offset="1" stop-color="#0b3f96"/></linearGradient></defs>
    <path d="M0 70 C120 20 260 110 400 22 L400 110 L0 110 Z" fill="url(#gLh)"/>
    <path d="M0 58 C120 8 260 98 400 10" fill="none" stroke="#0d0d0d" stroke-width="2"/>
  </svg>
</section>

<section class="sheet folder" aria-label="Presentation folder">
  <span class="dot"></span>
  <div class="name">
    <div class="brand">QUORVIX</div>
    <div class="tagline">Circuitry Supply Partners, LLC.</div>
  </div>
  <svg class="wave" viewBox="0 0 400 110" preserveAspectRatio="none" height="130">
    <defs><linearGradient id="gFd" x1="0" y1="0" x2="0" y2="1"><stop offset="0" stop-color="#3c9bf0"/><stop offset="1" stop-color="#0b3f96"/></linearGradient></defs>
    <path d="M0 72 C120 22 260 110 400 22 L400 110 L0 110 Z" fill="url(#gFd)"/>
    <path d="M0 60 C120 10 260 98 400 10" fill="none" stroke="#0d0d0d" stroke-width="2"/>
  </svg>
</section>

<section class="sheet card card-front" aria-label="Business card front">
  <div class="logo"><span class="dot"></span><span class="brand">QUORVIX</span></div>
  <div class="details">
    <strong>Paul Dunmore</strong><br>President<br>555-010-2040<br>mark@quorvix.com
  </div>
  <svg class="wave" viewBox="0 0 400 110" preserveAspectRatio="none" height="40">
    <defs><linearGradient id="gCf" x1="0" y1="0" x2="0" y2="1"><stop offset="0" stop-color="#3c9bf0"/><stop offset="1" stop-color="#0b3f96"/></linearGradient></defs>
    <path d="M120 110 C220 80 300 40 400 20 L400 110 Z" fill="url(#gCf)"/>
    <path d="M110 100 C210 70 300 28 400 8" fill="none" stroke="#0d0d0d" stroke-width="3"/>
  </svg>
</section>

<section class="sheet card card-back" aria-label="Business card back">
  <span class="dot"></span>
  <div class="web">www.quorvix.com</div>
  <svg class="wave" viewBox="0 0 400 110" preserveAspectRatio="none" height="40">
    <defs><linearGradient id="gCb" x1="0" y1="0" x2="0" y2="1"><stop offset="0" stop-color="#3c9bf0"/><stop offset="1" stop-color="#0b3f96"/></linearGradient></defs>
    <path d="M120 110 C220 80 300 40 400 20 L400 110 Z" fill="url(#gCb)"/>
    <path d="M110 100 C210 70 300 28 400 8" fill="none" stroke="#0d0d0d" stroke-width="3"/>
  </svg>
</section>

<section class="sheet envelope envelope-front" aria-label="Envelope front">
  <div class="logo"><span class="dot"></span>
    <div><div class="brand">QUORVIX</div><div class="tagline">Circuitry Supply Partners, LLC.</div></div>
  </div>
  <div class="return">457 Ridgeback Ave. Fernvale, QX 58204</div>
</section>

<section class="sheet envelope envelope-back" aria-label="Envelope back">
  <svg class="flap" viewBox="0 0 436 172" preserveAspectRatio="none">
    <defs><linearGradient id="gEn" x1="0" y1="0" x2="0" y2="1"><stop offset="0" stop-color="#0b3f96"/><stop offset="1" stop-color="#3c9bf0"/></linearGradient></defs>
    <path d="M0 0 L436 0 L436 80 L218 120 L0 80 Z" fill="url(#gEn)"/>
    <path d="M0 90 L218 130 L436 90" fill="none" stroke="#cfd3d8" stroke-width="1"/>
  </svg>
  <div class="web">www.quorvix.com</div>
</section>

</body>
</html>
```